Construction Company Website Design

I need a Website Design for a Construction Company. I have attached logo and business card design files (a.i) to match styles and text for the website. I will need design for 3 pages:
1. A Home page
2. A secondary page (will be different information pages)
3. A contact page with submision form
Website to look professional and match the 'theme' across all pages, using main colours / reverse colours as per design files. Must be clear it is a construction related website without being over the top. Happy for the construction related details (whether that be images/outlines/backgrounds etc to be fairly subtle and not overbearing on the contect of the pages. It will be the content that will be most important, not the images within.

Content has not yet been fully completed but attached is a site map. Each page will need a space for the insertion of the relevant heading and associated content for that particular page. Example can be used as per attached map. If it is preferable to have content completed for this to be a more succesful project please advise and I will complete and submit.

Target Market(s)

Clients for potential construction projects. These could be a range of people. All would be very professional, well educated and put a substantial expection on the quality of website provided.

Industry/Entity Type

Construction

Number of Pages Required

3 page

Font styles to use
Serif
Sans Serif
Other font styles liked:
• fonts preferable as per design files provided unless designer beleives a different font would suit better

Requirements
Must have
• Colour scheme to match logo and business card files provided. Fonts that match as per provided files. Pages must be consistent with the theme carrying across all pages. All pages must have contact details at the bottom of the page.
• Contents of page 1 - 'Home page': multiple tab options / logo link
• Contents of page 2 - 'Secondary page': Top and side navigation / area for information and/or images.
• Contents of page - 'Contact us page': Top and side navigation / Submission form / area for logos such as linkdin, facebook etc.
Nice to have
• Would be good to have a or some generic construction related images - outlines / shadows / effects etc. These might be background images or outlines related to the relevant industry and are consistent across the pages. Could be outlines of buildings, images of men with hardhats etc etc. Good to see colour scheme as per design files used
Should not have
• No pictures of houses. Generally no photos. If any imagery of people must not show faces/details.

```html
<!DOCTYPE html>
<html lang="en">
<head>
<meta charset="utf-8">
<title>Northgate Builders</title>
<link href="https://fonts.googleapis.com/css2?family=Open+Sans:wght@400;600;700&display=swap" rel="stylesheet">
<style>
:root{
  --blue:#00a9e6;
  --ink:#333a40;
  --text:#6a6f74;
  --light:#f2f3f5;
  --line:#cfd4d8;
  --footer:#2b2b2b;
  --footer-deep:#1d1d1d;
  --white:#ffffff;
}
*{margin:0;padding:0;box-sizing:border-box}
html,body{width:1200px;height:3297px;overflow:hidden}
body{font-family:"Open Sans",Arial,sans-serif;color:var(--ink);background:var(--white);position:relative}
section,header,footer{position:absolute;left:0;width:1200px}
.abs{position:absolute}

/* header */
.site-header{top:0;height:79px;background:rgba(255,255,255,.96);z-index:2;box-shadow:0 1px 3px rgba(0,0,0,.08)}
.brand{left:72px;top:28px;display:flex;align-items:center;gap:10px;font-weight:600;font-size:17px;letter-spacing:2px;color:var(--ink)}
.brand-mark{width:12px;height:12px;background:var(--blue)}
.main-nav{left:486px;top:0;height:79px;display:flex}
.main-nav a{display:flex;align-items:center;height:79px;padding:0 14px;font-size:14px;font-weight:600;color:var(--ink);text-decoration:none;text-transform:uppercase;margin-right:6px}
.main-nav a.active{background:var(--blue);color:var(--white)}
.caret{margin-left:6px;width:8px;height:8px}

/* hero */
.hero{top:79px;height:492px;background:linear-gradient(180deg,#1b3a66 0%,#2c4f7e 35%,#5c5f66 70%,#8b7f73 100%)}
.hero-copy{left:0;top:140px;width:1200px;text-align:center;color:var(--white)}
.hero-title{font-size:52px;font-weight:600;letter-spacing:4px;line-height:62px}
.hero-sub{font-size:21px;font-weight:700;letter-spacing:1px;line-height:28px;margin-top:8px}

/* about */
.about{top:571px;height:425px;background:var(--white)}
.about-art{left:0;top:0;width:540px;height:425px;background:linear-gradient(135deg,#f7f8fa 0%,#e3e7ec 60%,#c9d0d8 100%)}
.section-title{font-size:37px;font-weight:600;color:var(--ink);letter-spacing:1px}
.about .section-title{left:563px;top:52px}
.about-text{left:563px;top:120px;width:555px;font-size:13.5px;line-height:21px;color:var(--text)}
.about-text p+p{margin-top:19px}
.btn{display:flex;align-items:center;justify-content:center;background:var(--blue);color:var(--white);font-size:15px;font-weight:700;text-transform:uppercase;letter-spacing:.5px}
.about .btn{left:561px;top:328px;width:157px;height:42px}

/* services */
.services{top:996px;height:411px;background:var(--light)}
.centered{left:0;width:1200px;text-align:center}
.services .section-title{top:54px}
.service-card{top:187px;width:244px;height:167px;background:rgba(255,255,255,.7);border:1.5px solid #7fd1ee;text-align:center;padding:46px 12px 0}
.service-card h3{font-size:14px;font-weight:700;text-transform:uppercase;color:#222;letter-spacing:.3px}
.service-card p{font-size:14px;line-height:21px;color:#333;margin-top:4px}
.service-icon{top:143px;width:79px;height:79px;background:var(--blue);display:flex;align-items:center;justify-content:center;z-index:1}

/* projects */
.projects{top:1407px;height:864px;background:var(--white)}
.projects .section-title{top:54px}
.filter{top:143px;height:24px;border:1px solid #b9bec3;font-size:12px;display:flex;align-items:center;justify-content:center;color:#444;text-transform:uppercase}
.filter.on{background:var(--blue);border-color:var(--blue);color:var(--white)}
.tile{width:264px;height:243px}
.projects .btn{left:523px;top:767px;width:158px;height:39px}

/* news */
.news{top:2271px;height:646px;background:linear-gradient(180deg,#f4f5f7,#eceef1)}
.news .section-title{top:54px}
.news-card{top:140px;width:515px;height:343px;background:var(--white);box-shadow:0 2px 6px rgba(0,0,0,.15)}
.news-media{left:0;top:0;width:515px;height:183px}
.date-badge{left:16px;top:16px;width:50px;height:79px;background:var(--blue);color:var(--white);text-align:center}
.date-badge b{display:block;font-size:31px;font-weight:600;line-height:40px;margin-top:2px}
.date-badge span{font-size:11px;text-transform:uppercase}
.news-body{left:18px;top:198px;width:480px}
.news-body h3{font-size:21px;font-weight:400;color:#111;white-space:nowrap}
.news-body p{font-size:14px;line-height:22px;color:#333;margin-top:8px}
.read-more{display:block;font-size:13.5px;font-weight:700;color:var(--blue);margin-top:12px}
.news .btn{left:521px;top:545px;width:158px;height:39px}

/* footer */
.site-footer{top:2917px;height:332px;background:var(--footer);color:var(--white)}
.footer-title{font-size:14.5px;font-weight:700;text-transform:uppercase;letter-spacing:.5px}
.quick-links{left:72px;top:41px}
.quick-links ul{list-style:none;margin-top:14px}
.quick-links li{font-size:13px;text-transform:uppercase;line-height:31.6px}
.address{left:371px;top:41px}
.address ul{list-style:none;margin-top:16px}
.address li{display:flex;align-items:center;gap:16px;font-size:13px;height:32px}
.address svg{width:14px;height:14px;flex:none}
.follow{left:371px;top:220px}
.social{left:371px;top:252px;display:flex;gap:6px}
.social span{width:40px;height:40px;border:1.5px solid #cfcfcf}
.social span.on{background:var(--blue);border-color:var(--blue)}
.contact-form{left:818px;top:41px;width:310px}
.field{height:32px;border:1.5px solid #cfcfcf;font-size:12px;padding:6px 10px;margin-top:12px}
.field:first-of-type{margin-top:20px}
.field.msg{height:75px}
.contact-form .btn{width:125px;height:31px;font-size:12px;margin-top:14px}
.legal{top:3249px;height:48px;background:var(--footer-deep);color:#d8d8d8;font-size:11px;display:flex;align-items:center;justify-content:center}
</style>
</head>
<body>

<header class="site-header">
  <div class="abs brand"><span class="brand-mark"></span>NORTHGATE BUILDERS</div>
  <nav class="abs main-nav">
    <a class="active">Home</a>
    <a>About Us</a>
    <a>Services<svg class="caret" viewBox="0 0 8 8"><path d="M1 2.5l3 3 3-3" fill="none" stroke="#333" stroke-width="1.4"/></svg></a>
    <a>Projects</a>
    <a>Culture</a>
    <a>News</a>
    <a>Contact</a>
  </nav>
</header>

<section class="hero" role="img" aria-label="Upward view of steel reinforcement bars on a building site against a blue sky">
  <div class="abs hero-copy">
    <h1 class="hero-title">WELCOME&nbsp; TO<br>NORTHGATE BUILDERS</h1>
    <p class="hero-sub">Lorem Ipsum is simply dummy text of the<br>printing and typesetting industry</p>
  </div>
</section>

<section class="about">
  <div class="abs about-art" role="img" aria-label="Pencil sketch of city buildings above rolled blueprints and drafting tools"></div>
  <h2 class="abs section-title">ABOUT US</h2>
  <div class="abs about-text">
    <p>Lorem Ipsum is simply dummy text of the printing and typesetting industry. Lorem Ipsum has been the industry's standard dummy text ever since the 1500s, when an unknown printer took a galley of type and scrambled it to make a type specimen book.Lorem Ipsum is simply dummy text of the printing andindustry.</p>
    <p>Lorem Ipsum has been the industry's standard dummy text ever since the 1500s, when an unknown printer took a galley of type and scrambled it to make a type specimen book.</p>
  </div>
  <div class="abs btn">Read More</div>
</section>

<section class="services">
  <h2 class="abs centered section-title">OUR SERVICES</h2>

  <div class="abs service-card" style="left:72px"><h3>Building Maintenance</h3><p>Lorem Ipsum is simply dummy text of the printing and typesetting industry.&nbsp; Lorem Ipsum is simply.</p></div>
  <div class="abs service-icon" style="left:154px"><svg width="44" height="44" viewBox="0 0 44 44" fill="none" stroke="#fff" stroke-width="2"><rect x="8" y="6" width="28" height="32" rx="2"/><path d="M15 15h14M15 22h14M15 29h9"/><path d="M17 4h10v5H17z"/></svg></div>

  <div class="abs service-card" style="left:343px"><h3>Project Management</h3><p>Lorem Ipsum is simply dummy text of the printing and typesetting industry.&nbsp; Lorem Ipsum is simply.</p></div>
  <div class="abs service-icon" style="left:425px"><svg width="44" height="44" viewBox="0 0 44 44" fill="none" stroke="#fff" stroke-width="2"><rect x="7" y="7" width="30" height="30" rx="2"/><path d="M13 29l7-8 5 5 7-10"/><path d="M13 14h8"/></svg></div>

  <div class="abs service-card" style="left:613px"><h3>Commercial</h3><p>Lorem Ipsum is simply dummy text of the printing and typesetting industry.&nbsp; Lorem Ipsum is simply.</p></div>
  <div class="abs service-icon" style="left:695px"><svg width="44" height="44" viewBox="0 0 44 44" fill="none" stroke="#fff" stroke-width="2"><path d="M12 20a10 10 0 0 1 20 0z"/><path d="M9 20h26"/><path d="M14 38c0-7 4-11 8-11s8 4 8 11"/></svg></div>

  <div class="abs service-card" style="left:884px"><h3>Residential</h3><p>Lorem Ipsum is simply dummy text of the printing and typesetting industry.&nbsp; Lorem Ipsum is simply.</p></div>
  <div class="abs service-icon" style="left:966px"><svg width="44" height="44" viewBox="0 0 44 44" fill="none" stroke="#fff" stroke-width="2"><rect x="9" y="6" width="26" height="32"/><path d="M14 12h4M26 12h4M14 19h4M26 19h4M14 26h4M26 26h4M19 38v-6h6v6"/></svg></div>
</section>

<section class="projects">
  <h2 class="abs centered section-title">PROJECTS</h2>
  <div class="abs filter on" style="left:464px;width:48px">All</div>
  <div class="abs filter" style="left:521px;width:103px">Residential</div>
  <div class="abs filter" style="left:633px;width:106px">Commercial</div>

  <div class="abs tile" style="left:72px;top:220px;background:linear-gradient(160deg,#bcd6ee,#8a9aa8 70%,#5d6066)" role="img" aria-label="Tower cranes over a building under construction"></div>
  <div class="abs tile" style="left:336px;top:220px;background:linear-gradient(160deg,#1d2d4a,#283a57 60%,#1a2438)" role="img" aria-label="Steel frame structure under a dark blue sky">
    <svg class="abs" style="left:107px;top:96px" width="50" height="50" viewBox="0 0 50 50" fill="none" stroke="#fff" stroke-width="1.5"><rect x="1" y="1" width="48" height="48"/><circle cx="23" cy="22" r="8"/><path d="M29 28l7 7"/></svg>
  </div>
  <div class="abs tile" style="left:600px;top:220px;background:linear-gradient(160deg,#e2dcd2,#c9b79a 60%,#b08f5c)" role="img" aria-label="Plans on a desk with a calculator, rulers and tools"></div>
  <div class="abs tile" style="left:864px;top:220px;background:linear-gradient(160deg,#d7a24d,#b9812f 50%,#7c6a58)" role="img" aria-label="Worker holding a yellow hard hat"></div>
  <div class="abs tile" style="left:72px;top:463px;background:linear-gradient(160deg,#9fc3e3,#a59f93 60%,#c7b36e)" role="img" aria-label="White hard hat in front of a crane and building"></div>
  <div class="abs tile" style="left:336px;top:463px;background:linear-gradient(160deg,#7a6a88,#c28b88 60%,#2a2226)" role="img" aria-label="Silhouette of a steel truss against a dusk sky"></div>
  <div class="abs tile" style="left:600px;top:463px;background:linear-gradient(160deg,#e7a05a,#b8683a 55%,#2b1f1c)" role="img" aria-label="Steel beams being lifted at sunset"></div>
  <div class="abs tile" style="left:864px;top:463px;background:linear-gradient(160deg,#e5c08f,#a77a4c 55%,#3d2c22)" role="img" aria-label="Scaffolding and reinforcement columns at sunrise"></div>

  <div class="abs btn">View More</div>
</section>

<section class="news">
  <h2 class="abs centered section-title">NEWS</h2>

  <article class="abs news-card" style="left:72px">
    <div class="abs news-media" style="background:linear-gradient(150deg,#d7c7a8,#c99a5a 50%,#e9c23a)" role="img" aria-label="Hard hat, tools and bricks on construction plans"></div>
    <div class="abs date-badge"><b>30</b><span>July</span></div>
    <div class="abs news-body">
      <h3>Ipsum is simply dummy text of the printing</h3>
      <p>Lorem Ipsum is simply dummy text of the printing and typesetting industry.&nbsp; Lorem Ipsum is simply.</p>
      <span class="read-more">Read More</span>
    </div>
  </article>

  <article class="abs news-card" style="left:613px">
    <div class="abs news-media" style="background:linear-gradient(150deg,#f2f2f2,#cfd1d3 55%,#e3c34a)" role="img" aria-label="Screwdriver and tools lying on a floor plan"></div>
    <div class="abs date-badge"><b>30</b><span>July</span></div>
    <div class="abs news-body">
      <h3>Simply dummy text of the printing and</h3>
      <p>Lorem Ipsum is simply dummy text of the printing and typesetting industry.&nbsp; Lorem Ipsum is simply.</p>
      <span class="read-more">Read More</span>
    </div>
  </article>

  <div class="abs btn">View More</div>
</section>

<footer class="site-footer">
  <div class="abs quick-links">
    <h4 class="footer-title">Quick Links</h4>
    <ul><li>Home</li><li>About Us</li><li>Services</li><li>Projects</li><li>Culture</li><li>News</li><li>Contact</li></ul>
  </div>

  <div class="abs address">
    <h4 class="footer-title">Our Address</h4>
    <ul>
      <li><svg viewBox="0 0 14 14"><rect x="1" y="3" width="12" height="9" rx="1" fill="#fff"/><rect x="4" y="1" width="6" height="3" fill="#fff"/></svg>0400 123 456</li>
      <li><svg viewBox="0 0 14 14"><path d="M7 1a4 4 0 0 1 4 4c0 3-4 8-4 8S3 8 3 5a4 4 0 0 1 4-4z" fill="#fff"/><circle cx="7" cy="5" r="1.5" fill="#2b2b2b"/></svg>14 Harbour Street Lindfield 2070</li>
      <li><svg viewBox="0 0 14 14"><rect x="1" y="3" width="12" height="9" fill="#fff"/><path d="M1 3l6 5 6-5" fill="none" stroke="#2b2b2b" stroke-width="1.2"/></svg>info@northgatebuilders.com.au</li>
      <li><svg viewBox="0 0 14 14"><circle cx="7" cy="7" r="6" fill="#fff"/><path d="M1 7h12M7 1c-3 3-3 9 0 12M7 1c3 3 3 9 0 12" fill="none" stroke="#2b2b2b" stroke-width="1"/></svg>www.northgatebuilders.com.au</li>
    </ul>
  </div>
  <h4 class="abs footer-title follow">Follow Us</h4>
  <div class="abs social" aria-label="Social links">
    <span></span><span></span><span class="on"></span><span></span>
  </div>

  <div class="abs contact-form">
    <h4 class="footer-title">Contact Us</h4>
    <div class="field">Name</div>
    <div class="field">Phone</div>
    <div class="field msg">Message</div>
    <div class="btn">Send</div>
  </div>
</footer>

<div class="abs legal" style="left:0;width:1200px">Northgate Builders © 2017. All rights reserved. Terms and Conditions - Privacy Policy.</div>

</body>
</html>
```